table invoices in a modern format! (make it fun to look at!!)

Our has invoices that are shown to our clients. This is currently done in a normal table view, but its boring to look at and is not modern.
We would like to have a modern look and feel
it should ABSOLUTLY not be in table form.
Cards, graphs, pictures, whatever... should be fun and almost interactive.

the table file is how it current looks like.
the other two files were "ideas" to have a better representation
IT DOES NOT NEED TO LOOK LIKE THAT if you have a better idea please go for it.

secondary objective, the graphs/cards/whatever you design should be interactive, meaning I can "click on it" to pay a bill, or see more info.

Let me know if there are more questions!

```html
<!DOCTYPE html>
<html lang="en">
<head>
<meta charset="utf-8">
<title>Invoices 2019</title>
<link href="https://fonts.googleapis.com/css2?family=Source+Sans+3:wght@300;400;600;700&display=swap" rel="stylesheet">
<style>
  :root{
    --ink:#2b2b2b;
    --muted:#a9a9a9;
    --rule:#dedede;
    --yellow:#ffbf0f;
    --yellow-soft:#ffe08a;
    --green:#33cc44;
    --green-soft:#a8e6b0;
    --red:#f0283c;
    --red-soft:#f59aa4;
    --planned:#dcdcdc;
    --blue:#3478b8;
    --pink:#ee5a88;
    --lime:#9acd1a;
    --cyan:#12b5e5;
    --band:#8a8a8a;
  }
  html,body{margin:0;padding:0;width:861px;height:1200px;overflow:hidden;background:#fff}
  svg{display:block;font-family:"Source Sans 3",sans-serif}
  .title{font-size:48px;font-weight:300;fill:var(--ink);text-anchor:middle}
  .nav{font-size:10px}
  .month{font-size:15px;font-weight:700;fill:var(--ink);text-anchor:middle}
  .card{fill:#fff;stroke:var(--rule);stroke-width:1.2}
  .pill{fill:#fff;stroke-width:1.4}
  .pill-text{font-size:13px;font-weight:700;text-anchor:middle}
  .amount{font-size:21px;fill:var(--ink);text-anchor:middle}
  .amount tspan{font-size:16px}
  .ref{font-size:10px;fill:var(--muted);text-anchor:middle}
  .axis{font-size:10px;fill:var(--muted);text-anchor:end}
  .grid{stroke:#e3e3e3;stroke-dasharray:6 5}
  .price{fill:var(--blue)}
  .extra{fill:var(--pink)}
  .paid-line{fill:none;stroke:var(--lime);stroke-width:3;stroke-linejoin:round}
  .paid-dot{fill:var(--lime)}
  .col{font-size:11px;fill:var(--ink);text-anchor:middle}
  .cell{font-size:10px;fill:var(--ink);text-anchor:middle}
  .cell-b{font-size:10px;font-weight:700;text-anchor:middle}
  .legend{font-size:11px;font-weight:700;fill:var(--ink)}
  .row-rule{stroke:var(--rule)}
  .tip{fill:#fff;stroke-width:1.3}
  .tip-label{font-size:10px;fill:var(--ink);text-anchor:middle}
  .tip-amount{font-size:15px;font-weight:700;text-anchor:middle}
  .tip-amount tspan{font-size:10px}
  .tip-note{font-size:9px;fill:var(--red);text-anchor:middle}
  .pay-btn{fill:var(--cyan)}
  .pay-text{font-size:13px;font-weight:700;fill:#fff;text-anchor:middle}
</style>
</head>
<body>
<svg width="861" height="1200" viewBox="0 0 1440 2007" role="img" aria-label="Invoices 2019 overview with timeline cards and monthly chart">
  <defs>
    <clipPath id="board-clip"><rect x="0" y="0" width="1392" height="950"/></clipPath>
    <filter id="lift" x="-20%" y="-10%" width="140%" height="125%">
      <feDropShadow dx="0" dy="2" stdDeviation="4" flood-color="#000" flood-opacity="0.15"/>
    </filter>

    <g id="board">
      <text class="title" x="720" y="112">INVOICES 2019</text>
      <line x1="688" y1="129" x2="752" y2="129" stroke="#cfcfcf" stroke-width="3"/>

      <g class="pager">
        <text class="nav" x="1314" y="166" fill="#cfcfcf" text-anchor="middle">PREV</text>
        <path d="M1336 173H1290M1296 168l-6 5 6 5" stroke="#cfcfcf" stroke-width="1.5" fill="none"/>
        <text class="nav" x="1366" y="166" fill="var(--cyan)" text-anchor="middle">NEXT</text>
        <path d="M1344 173H1390M1384 168l6 5-6 5" stroke="var(--cyan)" stroke-width="1.5" fill="none"/>
      </g>

      <g clip-path="url(#board-clip)">
        <line x1="48" y1="232" x2="1400" y2="232" stroke="#333" stroke-width="2"/>

        <g class="months">
          <text class="month" x="120" y="207">Jan.</text>
          <text class="month" x="276" y="207">Feb.</text>
          <text class="month" x="432" y="207">Mar.</text>
          <text class="month" x="588" y="207">Apr.</text>
          <text class="month" x="744" y="207">May</text>
          <text class="month" x="900" y="207">Jun.</text>
          <text class="month" x="1056" y="207">Jul.</text>
          <text class="month" x="1212" y="207">Aug.</text>
          <text class="month" x="1368" y="207">Sep.</text>
        </g>

        <g class="status-dots">
          <circle cx="120" cy="232" r="10" fill="var(--yellow)"/><circle cx="120" cy="256" r="5" fill="var(--yellow-soft)"/>
          <circle cx="276" cy="232" r="10" fill="var(--green)"/><circle cx="276" cy="256" r="5" fill="var(--green-soft)"/>
          <circle cx="432" cy="232" r="10" fill="var(--green)"/><circle cx="432" cy="256" r="5" fill="var(--green-soft)"/>
          <circle cx="588" cy="232" r="10" fill="var(--red)"/><circle cx="588" cy="256" r="5" fill="var(--red-soft)"/>
          <circle cx="744" cy="232" r="10" fill="var(--yellow)"/><circle cx="744" cy="256" r="5" fill="var(--yellow-soft)"/>
          <circle cx="900" cy="232" r="10" fill="var(--green)"/><circle cx="900" cy="256" r="5" fill="var(--green-soft)"/>
          <circle cx="1056" cy="232" r="10" fill="var(--green)"/><circle cx="1056" cy="256" r="5" fill="var(--green-soft)"/>
          <circle cx="1212" cy="232" r="10" fill="var(--red)"/><circle cx="1212" cy="256" r="5" fill="var(--red-soft)"/>
          <circle cx="1368" cy="232" r="10" fill="var(--planned)"/><circle cx="1368" cy="256" r="5" fill="#eeeeee"/>
        </g>

        <g class="invoice-cards">
          <rect class="card" x="48" y="282" width="143" height="104" rx="4"/>
          <rect class="card" x="204" y="282" width="143" height="104" rx="4"/>
          <rect class="card" x="360" y="282" width="143" height="104" rx="4"/>
          <rect class="card" x="516" y="282" width="143" height="104" rx="4"/>
          <rect class="card" x="672" y="282" width="143" height="104" rx="4"/>
          <rect class="card" x="828" y="282" width="143" height="104" rx="4"/>
          <rect class="card" x="984" y="282" width="143" height="104" rx="4"/>
          <rect class="card" x="1140" y="282" width="143" height="104" rx="4"/>
          <rect class="card" x="1296" y="282" width="143" height="104" rx="4"/>

          <rect class="pill" x="77" y="271" width="86" height="22" rx="11" stroke="var(--yellow)"/>
          <text class="pill-text" x="120" y="287" fill="var(--yellow)">PARTIAL</text>
          <rect class="pill" x="246" y="271" width="60" height="22" rx="11" stroke="var(--green)"/>
          <text class="pill-text" x="276" y="287" fill="var(--green)">PAID</text>
          <rect class="pill" x="402" y="271" width="60" height="22" rx="11" stroke="var(--green)"/>
          <text class="pill-text" x="432" y="287" fill="var(--green)">PAID</text>
          <rect class="pill" x="549" y="271" width="78" height="22" rx="11" stroke="var(--red)"/>
          <text class="pill-text" x="588" y="287" fill="var(--red)">UNPAID</text>
          <rect class="pill" x="701" y="271" width="86" height="22" rx="11" stroke="var(--yellow)"/>
          <text class="pill-text" x="744" y="287" fill="var(--yellow)">PARTIAL</text>
          <rect class="pill" x="870" y="271" width="60" height="22" rx="11" stroke="var(--green)"/>
          <text class="pill-text" x="900" y="287" fill="var(--green)">PAID</text>
          <rect class="pill" x="1026" y="271" width="60" height="22" rx="11" stroke="var(--green)"/>
          <text class="pill-text" x="1056" y="287" fill="var(--green)">PAID</text>
          <rect class="pill" x="1173" y="271" width="78" height="22" rx="11" stroke="var(--red)"/>
          <text class="pill-text" x="1212" y="287" fill="var(--red)">UNPAID</text>
          <rect class="pill" x="1328" y="271" width="84" height="22" rx="11" stroke="var(--planned)"/>
          <text class="pill-text" x="1370" y="287" fill="#cfcfcf">PLANNED</text>

          <text class="amount" x="120" y="334">€1293.<tspan>18</tspan></text>
          <text class="amount" x="276" y="334">€1152.<tspan>00</tspan></text>
          <text class="amount" x="432" y="334">€1248.<tspan>00</tspan></text>
          <text class="amount" x="588" y="334">€955.<tspan>91</tspan></text>
          <text class="amount" x="744" y="334">€609.<tspan>24</tspan></text>
          <text class="amount" x="900" y="334">€538.<tspan>71</tspan></text>
          <text class="amount" x="1056" y="334">€829.<tspan>39</tspan></text>
          <text class="amount" x="1212" y="334">€1222.<tspan>65</tspan></text>
          <text class="amount" x="1368" y="334" fill="#cfcfcf" style="fill:#cfcfcf">€591.<tspan>13</tspan></text>

          <text class="ref" x="120" y="354">TKZ19-0037</text>
          <text class="ref" x="276" y="354">TKZ19-0103</text>
          <text class="ref" x="432" y="354">TKZ19-0355</text>
          <text class="ref" x="588" y="354">TKZ19-0354</text>
          <text class="ref" x="744" y="354">TKZ19-0306</text>
          <text class="ref" x="900" y="354">TKZ19-0398</text>
          <text class="ref" x="1056" y="354">TKZ19-0479</text>
          <text class="ref" x="1212" y="354">TKZ19-0547</text>
        </g>
      </g>

      <g class="chart">
        <line x1="137" y1="452" x2="137" y2="872" stroke="var(--rule)"/>
        <text class="axis" x="127" y="459">€</text>
        <line class="grid" x1="137" y1="515" x2="1392" y2="515"/>
        <line class="grid" x1="137" y1="579" x2="1392" y2="579"/>
        <line class="grid" x1="137" y1="643" x2="1392" y2="643"/>
        <line class="grid" x1="137" y1="707" x2="1392" y2="707"/>
        <text class="axis" x="128" y="519">1200</text>
        <text class="axis" x="128" y="583">900</text>
        <text class="axis" x="128" y="647">600</text>
        <text class="axis" x="128" y="711">300</text>

        <rect class="price" x="175" y="525" width="32" height="246"/>
        <rect class="extra" x="175" y="495" width="32" height="30"/>
        <rect class="price" x="279" y="525" width="32" height="246"/>
        <rect class="price" x="384" y="505" width="32" height="266"/>
        <rect class="price" x="488" y="567" width="32" height="204"/>
        <rect class="price" x="593" y="641" width="32" height="130"/>
        <rect class="price" x="697" y="669" width="32" height="102"/>
        <rect class="extra" x="697" y="656" width="32" height="13"/>
        <rect class="price" x="802" y="595" width="32" height="176"/>
        <rect class="price" x="906" y="510" width="32" height="261"/>
        <rect class="price" x="1011" y="664" width="32" height="107"/>
        <rect class="extra" x="1011" y="645" width="32" height="19"/>
        <rect class="price" x="1115" y="610" width="32" height="161"/>
        <rect class="price" x="1220" y="716" width="32" height="55"/>
        <rect class="price" x="1324" y="563" width="32" height="208"/>

        <polyline class="paid-line" points="191,506 295,506 400,505 504,771 609,655 713,574 818,463 922,771"/>
        <circle class="paid-dot" cx="191" cy="506" r="4"/>
        <circle class="paid-dot" cx="295" cy="506" r="4"/>
        <circle class="paid-dot" cx="400" cy="505" r="4"/>
        <circle class="paid-dot" cx="504" cy="771" r="4"/>
        <circle class="paid-dot" cx="609" cy="655" r="4"/>
        <circle class="paid-dot" cx="713" cy="574" r="4"/>
        <circle class="paid-dot" cx="818" cy="463" r="4"/>
        <circle class="paid-dot" cx="922" cy="771" r="4"/>
      </g>

      <g class="chart-table">
        <line x1="48" y1="771" x2="1392" y2="771" stroke="#cccccc" stroke-width="1.5"/>
        <line class="row-rule" x1="48" y1="797" x2="1392" y2="797"/>
        <line class="row-rule" x1="48" y1="822" x2="1392" y2="822"/>
        <line class="row-rule" x1="48" y1="847" x2="1392" y2="847"/>
        <line class="row-rule" x1="48" y1="872" x2="1392" y2="872"/>

        <text class="col" x="191" y="789">January</text>
        <text class="col" x="295" y="789">February</text>
        <text class="col" x="400" y="789">March</text>
        <text class="col" x="504" y="789">April</text>
        <text class="col" x="609" y="789">May</text>
        <text class="col" x="713" y="789">June</text>
        <text class="col" x="818" y="789">July</text>
        <text class="col" x="922" y="789">August</text>
        <text class="col" x="1027" y="789">September</text>
        <text class="col" x="1131" y="789">October</text>
        <text class="col" x="1236" y="789">November</text>
        <text class="col" x="1340" y="789">December</text>

        <rect x="72" y="804" width="11" height="11" fill="var(--blue)"/>
        <text class="legend" x="88" y="815">PRICE</text>
        <rect x="69" y="829" width="11" height="11" fill="var(--pink)"/>
        <text class="legend" x="85" y="840">EXTRA</text>
        <line x1="67" y1="860" x2="91" y2="860" stroke="var(--lime)" stroke-width="3"/>
        <text class="legend" x="95" y="865">PAID</text>

        <text class="cell" x="191" y="815">1152.00</text>
        <text class="cell" x="295" y="815">1152.00</text>
        <text class="cell" x="400" y="815">1248.00</text>
        <text class="cell" x="504" y="815">955.91</text>
        <text class="cell" x="609" y="815">609.24</text>
        <text class="cell" x="713" y="815">478.85</text>
        <text class="cell" x="818" y="815">823.39</text>
        <text class="cell" x="922" y="815">1222.65</text>
        <text class="cell" x="1027" y="815">500.24</text>
        <text class="cell" x="1131" y="815">754.00</text>
        <text class="cell" x="1236" y="815">258.00</text>
        <text class="cell" x="1340" y="815">975.00</text>

        <text class="cell" x="191" y="840">141.18</text>
        <text class="cell" x="295" y="840">0.00</text>
        <text class="cell" x="400" y="840">0.00</text>
        <text class="cell" x="504" y="840">0.00</text>
        <text class="cell" x="609" y="840">0.00</text>
        <text class="cell" x="713" y="840">59.86</text>
        <text class="cell" x="818" y="840">0.00</text>
        <text class="cell" x="922" y="840">0.00</text>
        <text class="cell" x="1027" y="840">90.89</text>
        <text class="cell" x="1131" y="840">0.00</text>
        <text class="cell" x="1236" y="840">0.00</text>
        <text class="cell" x="1340" y="840">0.00</text>

        <text class="cell-b" x="191" y="865" fill="var(--yellow)">1243.20</text>
        <text class="cell-b" x="295" y="865" fill="var(--green)">1243.20</text>
        <text class="cell-b" x="400" y="865" fill="var(--ink)">1248.00</text>
        <text class="cell-b" x="504" y="865" fill="var(--red)">0.00</text>
        <text class="cell-b" x="609" y="865" fill="var(--yellow)">546.61</text>
        <text class="cell-b" x="713" y="865" fill="var(--green)">925.00</text>
        <text class="cell-b" x="818" y="865" fill="var(--green)">1444.00</text>
        <text class="cell-b" x="922" y="865" fill="var(--red)">0.00</text>
      </g>
    </g>
  </defs>

  <g class="state-default"><use href="#board"/></g>

  <rect class="divider-band" x="0" y="953" width="1440" height="100" fill="var(--band)"/>

  <g class="state-interactive">
    <use href="#board" y="1053"/>

    <g class="pdf-column">
      <rect x="348" y="1480" width="104" height="343" fill="#cfe9f7" fill-opacity="0.25"/>
      <rect x="348" y="1480" width="104" height="23" fill="#d6eef9"/>
      <path d="M384 1487h6l3 3v8h-9z" fill="var(--cyan)"/>
      <text x="397" y="1497" font-size="11" fill="var(--cyan)">PDF</text>
    </g>

    <g class="invoice-detail" filter="url(#lift)">
      <rect x="48" y="1335" width="143" height="272" rx="4" fill="#fff" stroke="#e2e2e2"/>
    </g>
    <g class="invoice-detail-body">
      <rect class="pill" x="77" y="1324" width="86" height="22" rx="11" stroke="var(--yellow)"/>
      <text class="pill-text" x="120" y="1340" fill="var(--yellow)">PARTIAL</text>
      <text class="amount" x="120" y="1387">€1293.<tspan>18</tspan></text>
      <text class="ref" x="120" y="1407">TKZ19-0037</text>
      <line x1="61" y1="1440" x2="179" y2="1440" stroke="var(--rule)"/>
      <text class="tip-label" x="120" y="1464">PAID</text>
      <text x="120" y="1483" font-size="14" fill="var(--ink)" text-anchor="middle">€1243.<tspan font-size="10">20</tspan></text>
      <line x1="61" y1="1500" x2="179" y2="1500" stroke="var(--rule)"/>
      <text class="tip-label" x="120" y="1524">REMAINING</text>
      <text class="tip-amount" x="120" y="1543" fill="var(--red)">€49.<tspan>98</tspan></text>
      <text class="tip-note" x="120" y="1557">225 days late</text>
      <rect class="pay-btn" x="80" y="1568" width="80" height="22" rx="11"/>
      <text class="pay-text" x="120" y="1584">PAY</text>
    </g>

    <g class="tooltip tooltip-open">
      <rect class="tip" x="661" y="1836" width="104" height="59" rx="4" stroke="var(--green)"/>
      <path d="M706 1895l7 8 7-8" fill="#fff" stroke="var(--green)" stroke-width="1.3"/>
      <line x1="707" y1="1895" x2="719" y2="1895" stroke="#fff" stroke-width="2"/>
      <text class="tip-label" x="713" y="1860">OPEN</text>
      <text class="tip-amount" x="713" y="1879" fill="var(--green)">€386.<tspan>29</tspan></text>
    </g>

    <g class="tooltip tooltip-unpaid">
      <rect class="tip" x="871" y="1787" width="103" height="108" rx="4" stroke="var(--red)"/>
      <path d="M915 1895l7 8 7-8" fill="#fff" stroke="var(--red)" stroke-width="1.3"/>
      <line x1="916" y1="1895" x2="928" y2="1895" stroke="#fff" stroke-width="2"/>
      <text class="tip-label" x="922" y="1812">UNPAID</text>
      <text class="tip-amount" x="922" y="1831" fill="var(--red)">€1222.<tspan>65</tspan></text>
      <text class="tip-note" x="922" y="1845">13 days late</text>
      <rect class="pay-btn" x="882" y="1856" width="80" height="22" rx="11"/>
      <text class="pay-text" x="922" y="1872">PAY</text>
    </g>
  </g>
</svg>
</body>
</html>
```